Business Card Design

We are a manufacturing company that has been in business for over 30 years, established in 1981. We are looking to increase our business with defence force, government, and the major telecoms so the card needs to present the company as being cutting edge, secure, and professional.
Industry/Entity Type
Defence
Contact Information for Business Card
Name Gareth Olsund
Phone 02 9374 6815
Fax 02 9457 3162
mobile 0438260517
Email Gary@Korvex.com.au
Webiste www.korvex.com.au
ABN 58 006 391 842
address: 17 Belcor Street Harwick Vale NSW 2874
"Manufacturer of Antennas, GPS, Microwave, Cable Assemblies, RF, Military, & Telecommunications"
Look and feel

```html
<!DOCTYPE html>
<html lang="en">
<head>
<meta charset="utf-8">
<title>Korvex Business Card</title>
<link href="https://fonts.googleapis.com/css2?family=Arimo:wght@400;700&display=swap" rel="stylesheet">
<style>
  :root {
    --navy: #1b2a5e;
    --brick: #c4462e;
    --paper: #ffffff;
    --stage: #e9e7e3;
    --ink-grey: #555a66;
    --mist: #dfe3ef;
  }
  * { box-sizing: border-box; margin: 0; padding: 0; }
  html, body {
    width: 1200px; height: 1000px; overflow: hidden;
    background: var(--stage);
    font-family: "Arimo", Arial, sans-serif;
  }
  .stage { position: relative; width: 1200px; height: 1000px; }
  .card {
    position: absolute; left: 300px; width: 600px; height: 343px;
    box-shadow: 0 6px 18px rgba(0,0,0,0.18);
    overflow: hidden;
  }
  .card--front { top: 120px; background: var(--paper); }
  .card--back { top: 530px; background: var(--navy); }

  /* Front */
  .brand { position: absolute; top: 26px; left: 34px; display: flex; align-items: center; gap: 10px; }
  .brand__square { width: 40px; height: 40px; background: var(--brick); }
  .brand__name { color: var(--navy); font-size: 16px; font-weight: 700; letter-spacing: 3px; }
  .contact { position: absolute; left: 300px; top: 92px; width: 270px; }
  .contact__name {
    color: var(--navy); font-size: 24px; font-weight: 700;
    letter-spacing: 2px; text-transform: uppercase; padding-bottom: 4px;
    border-bottom: 2px solid var(--brick); margin-bottom: 12px;
  }
  .contact__row { display: flex; color: var(--brick); font-size: 13px; line-height: 18px; }
  .contact__label { width: 92px; flex: none; }
  .abn {
    position: absolute; left: 22px; bottom: 16px;
    color: var(--ink-grey); font-size: 9px; letter-spacing: 0.5px;
  }

  /* Back */
  .tagline {
    position: absolute; top: 22px; right: 24px; width: 470px;
    color: var(--paper); text-align: right; text-transform: uppercase;
    font-size: 11.5px; letter-spacing: 1.2px; line-height: 16px;
  }
  .back-brand {
    position: absolute; left: 0; right: 0; top: 142px;
    display: flex; align-items: center; justify-content: center; gap: 14px;
  }
  .back-brand__square { width: 56px; height: 56px; background: var(--paper); }
  .back-brand__name { color: var(--paper); font-size: 22px; font-weight: 700; letter-spacing: 4px; }
  .website {
    position: absolute; left: 26px; bottom: 22px;
    color: var(--mist); font-size: 11px; letter-spacing: 4px;
  }
</style>
</head>
<body>
<main class="stage">
  <section class="card card--front" aria-label="Business card front">
    <div class="brand">
      <span class="brand__square"></span>
      <span class="brand__name">KORVEX</span>
    </div>
    <div class="contact">
      <h1 class="contact__name">Gareth Olsund</h1>
      <div class="contact__row"><span class="contact__label">Mobile:</span><span>0438260517</span></div>
      <div class="contact__row"><span class="contact__label">Phone:</span><span>02 9374 6815</span></div>
      <div class="contact__row"><span class="contact__label">Fax:</span><span>02 9457 3162</span></div>
      <div class="contact__row"><span class="contact__label">Email:</span><span>Gary@Korvex.com.au</span></div>
      <div class="contact__row"><span class="contact__label">Address:</span><span>17 Belcor Street<br>Harwick Vale<br>N.S.W. 2874</span></div>
    </div>
    <p class="abn">abn 58 006 391 842</p>
  </section>

  <section class="card card--back" aria-label="Business card back">
    <p class="tagline">Manufacturer of Antennas, GPS, Microwave,<br>Cable Assemblies, RF, Military, &amp; Telecommunications</p>
    <div class="back-brand">
      <span class="back-brand__square"></span>
      <span class="back-brand__name">KORVEX</span>
    </div>
    <p class="website">www.korvex.com.au</p>
  </section>
</main>
</body>
</html>
```